Drone service provider needs a brilliant web design

I need a responsive web design for a new drone service company. Pelwick Drone Solutions provides turnkey solutions to capture, process, and deliver actionable aerial data to customers. The design should communicate a professional company that is safe, legal and insured. I included our logo design and business card designs for reference.
*content to be supplied after design selected

Target Market(s)

We serve telecommunications, construction, government, utility infrastructure, insurance and other industries.

Industry/Entity Type

Industrial

Number of Pages Required

5+ page

Colors

Designer to choose colors to be used in the design.

Requirements
Must have
• The design should highlight professional services to include Inspections, Mapping, Consulting and Training. The site should include aerial images and video to compliment the services offered. The landing page must include following sections in order: HOME, SERVICES, ABOUT, DEMO REEL, CLIENTS, CONTACT FORM, and social media buttons (Facebook, LinkedIn, Twitter, YouTube, Instagram). Contact: 615-482-9031 info@pelwickdronesolutions.example Smyrna, TN
• Sitemap:
• 6 pages: Home, Inspections, Mapping, Training, Consulting, About
• HOME (Landing Page)
• • Header with logo and tab links (Home, Services, About, Contact)
• • 'CAPTURE. PROCESS. DELIVER.' tagline and 'CONTACT US' button displayed within aerial image of drone over city or construction site
• • Services section with icons, text and read more link to page
• • About section with photo and text with three icons for SAFE. LEGAL. INSURED.
• • Demo reel
• • Clients logos shown scrolling horizontally
• • Contact form
• • Footer with logo, phone, email, social media buttons
• SERVICES (4 different pages)
• • Inspections
• • Mapping
• • Consulting
• • Training
• ABOUT page
• • Company
• • Partners
• • Certifications & Associations
• • Careers
• CONTACT linked to bottom of landing page
• Would you like to receive the newsletter? Yes or No Drop-down list
Nice to have
• Photos of Orvex Talvan or Quillon inspecting infrastructure, buildings, construction sites, etc. A photo of one or two pilots in vest and helmet. Free stock photos preferred but would purchase the right photo that's more relevant.
• website references:
• https://www.brastelmoor.example/
• https://www.kestrimundo.example/services
• https://www.norblat.example/
• http://fenwoprisma.example/
• http://lumtorrex.example/
• http://gavrinoth.example/
• https://www.murbex.example/
Should not have
• not an aerial photography or videography service business, no blog or newsletter

```html
<!DOCTYPE html>
<html lang="en">
<head>
<meta charset="utf-8">
<title>Pelwick Drone Solutions</title>
<link rel="stylesheet" href="https://fonts.googleapis.com/css2?family=Exo+2:wght@600;700&family=Jost:wght@400;500;600&display=swap">
<style>
:root{
  --blue:#0b6fa8;
  --blue-deep:#075d8f;
  --ink:#1d1d1d;
  --text:#333;
  --dark:#303030;
  --topbar:#2f2f2f;
  --light:#f4f4f4;
  --white:#fff;
  --rule:#c9c9c9;
}
*{box-sizing:border-box;margin:0;padding:0}
html,body{width:1200px;height:2643px;overflow:hidden}
body{position:relative;font-family:"Jost",Arial,sans-serif;color:var(--text);background:var(--white)}
.abs{position:absolute}
.heading{font-family:"Exo 2",Arial,sans-serif;font-weight:700;color:var(--ink);letter-spacing:.5px}

/* top bar */
.topbar{left:0;top:0;width:1200px;height:42px;background:var(--topbar);color:#eee;font-size:15px}
.topbar .contact{position:absolute;top:11px;display:flex;align-items:center;gap:10px}
.topbar .phone{left:100px}
.topbar .mail{left:250px}
.topbar .sep{position:absolute;left:233px;top:15px;width:1px;height:12px;background:#777}
.social{display:flex;gap:6px}
.social span{width:28px;height:28px;border-radius:50%;background:var(--blue);border:2px solid #fff}
.topbar .social{position:absolute;right:96px;top:7px}

/* header */
.header{left:0;top:42px;width:1200px;height:108px;background:var(--white)}
.logo{font-family:"Exo 2",Arial,sans-serif;font-weight:700;color:var(--ink);display:flex;align-items:center;gap:12px}
.logo .dot{width:22px;height:22px;border-radius:50%;background:var(--blue)}
.logo .name{line-height:1}
.logo .name b{display:block;font-size:44px;letter-spacing:1px}
.logo .name small{display:block;font-size:16px;letter-spacing:4.2px;margin-top:4px;font-weight:700}
.header .logo{position:absolute;left:100px;top:22px}
.nav{position:absolute;top:40px;left:0;width:1200px;font-weight:600;font-size:17px;color:var(--ink);letter-spacing:.5px}
.nav a{position:absolute;color:inherit;text-decoration:none}
.nav .active{color:var(--blue)}
.nav .active::after{content:"";position:absolute;left:0;right:0;bottom:-10px;height:3px;background:var(--blue)}

/* hero */
.hero{left:0;top:150px;width:1200px;height:495px;background:linear-gradient(100deg,#e8772c 0%,#c9865a 22%,#7fa8cf 45%,#8fb8dc 70%,#6e8ca7 100%)}
.hero .arrow{position:absolute;top:185px}
.hero .caption{position:absolute;left:0;bottom:0;width:1200px;height:49px;background:rgba(40,40,40,.55);color:#fff;text-align:center;font-size:29px;line-height:49px;letter-spacing:1.5px}

/* about */
.about{left:0;top:645px;width:1200px;height:379px;background:var(--white);text-align:center}
.section-title{position:absolute;left:0;width:1200px;text-align:center;font-size:32px}
.section-title .accent{color:var(--blue)}
.section-title small{font-size:21px;color:var(--blue)}
.divider{position:absolute;left:465px;width:270px;height:1px;background:var(--rule)}
.divider::after{content:"";position:absolute;left:95px;top:-1px;width:80px;height:3px;background:var(--blue)}
.about p{position:absolute;left:102px;top:150px;width:996px;font-size:13.4px;line-height:24px;color:#444}
.btn{display:inline-flex;align-items:center;justify-content:space-between;background:var(--blue-deep);color:#fff;border-radius:20px;font-size:14px;font-weight:500;padding:0 4px 0 16px;text-decoration:none}
.btn i{width:24px;height:24px;border-radius:50%;background:#fff;display:flex;align-items:center;justify-content:center}
.about .btn{position:absolute;left:532px;top:266px;width:136px;height:38px;font-size:15px}

/* services */
.services{left:0;top:1024px;width:1200px;height:541px;background:var(--light)}
.service{position:absolute;top:166px;width:240px;margin-left:-120px;text-align:center}
.service .ring{width:130px;height:130px;margin:0 auto;border-radius:50%;border:4px solid #e2e2e2;background:#fff;display:flex;align-items:center;justify-content:center}
.service h3{font-size:21px;margin-top:23px}
.service p{font-size:13.5px;line-height:23px;color:#444;margin-top:10px}
.service .btn{margin-top:20px;width:115px;height:30px;font-size:11.5px;padding-left:14px;letter-spacing:.3px}
.service .btn i{width:22px;height:22px}

/* map */
.map{left:0;top:1565px;width:1200px;height:562px;background:linear-gradient(160deg,#eceae3 0%,#e4e6dc 45%,#dfe6d6 100%)}
.map .inset{position:absolute;left:396px;top:77px;width:407px;height:138px;border:4px solid #d8d8d8;background:linear-gradient(180deg,#8fb2d6 0%,#bfcfe0 45%,#3f6f98 70%,#55606a 100%)}

/* footer */
.footer{left:0;top:2127px;width:1200px;height:516px;background:var(--dark)}
.card-left{left:99px;top:1864px;width:502px;height:439px;background:var(--white);text-align:center}
.card-left .logo{justify-content:center;margin-top:76px}
.card-left h4{font-family:"Exo 2",Arial,sans-serif;font-weight:700;font-size:21px;color:var(--ink);margin-top:30px}
.card-left .social{justify-content:center;margin-top:12px}
.card-left p{font-size:14.5px;line-height:26px;color:#333;margin:40px auto 0;width:430px}
.card-right{left:601px;top:1864px;width:500px;height:439px;background:var(--blue)}
.card-right h2{position:absolute;left:40px;top:38px;font-family:"Exo 2",Arial,sans-serif;font-weight:700;font-size:26px;color:#fff;letter-spacing:.5px}
.card-right .bar{position:absolute;left:40px;top:83px;width:152px;height:2px;background:rgba(255,255,255,.35)}
.card-right .bar::after{content:"";position:absolute;left:0;top:0;width:68px;height:2px;background:#fff}
.field{position:absolute;left:40px;width:418px;border-bottom:1px solid rgba(255,255,255,.55);color:#fff;font-size:14px;padding-bottom:12px}
.submit{position:absolute;left:40px;top:356px;width:118px;height:36px;border-radius:18px;background:#2a2a2a;color:#fff;display:flex;align-items:center;justify-content:space-between;padding:0 5px 0 22px;font-size:15px;font-weight:500}
.submit i{width:26px;height:26px;border-radius:50%;background:#fff;display:flex;align-items:center;justify-content:center}
.footer-nav{left:0;top:2352px;width:1200px;font-weight:600;font-size:18px;color:#fff;letter-spacing:.5px}
.footer-nav a{position:absolute;color:inherit;text-decoration:none}
.info{position:absolute;top:2433px;width:400px;margin-left:-200px;text-align:center;color:#eee;font-size:15.5px}
.info .badge{width:56px;height:56px;margin:0 auto 18px;border-radius:50%;background:var(--blue);border:2px solid #fff;display:flex;align-items:center;justify-content:center}
.rule{left:99px;top:2583px;width:1002px;height:1px;background:#5a5a5a}
.copyright{left:0;top:2601px;width:1200px;text-align:center;color:#eee;font-size:14px}
</style>
</head>
<body>

<div class="abs topbar">
  <div class="contact phone">
    <svg width="16" height="16" viewBox="0 0 24 24"><path fill="#fff" d="M6.6 10.8a15 15 0 0 0 6.6 6.6l2.2-2.2c.3-.3.7-.4 1-.2 1.1.4 2.3.6 3.6.6.6 0 1 .4 1 1V20c0 .6-.4 1-1 1A17 17 0 0 1 3 4c0-.6.4-1 1-1h3.5c.6 0 1 .4 1 1 0 1.3.2 2.5.6 3.6.1.3 0 .7-.2 1z"/></svg>
    <span>615-482-9031</span>
  </div>
  <div class="sep"></div>
  <div class="contact mail">
    <svg width="18" height="14" viewBox="0 0 24 18"><rect x="1" y="1" width="22" height="16" rx="1" fill="#fff"/><path d="M2 2l10 8 10-8" stroke="#2f2f2f" stroke-width="2" fill="none"/></svg>
    <span>info@pelwickdronesolutions.example</span>
  </div>
  <div class="social" aria-label="Social media links"><span></span><span></span><span></span><span></span><span></span></div>
</div>

<header class="abs header">
  <div class="logo"><span class="dot"></span><span class="name"><b>PELWICK</b><small>DRONE SOLUTIONS</small></span></div>
  <nav class="nav">
    <a class="active" style="left:555px">HOME</a>
    <a style="left:671px">ABOUT US</a>
    <a style="left:828px">SERVICES</a>
    <a style="left:980px">CONTACT US</a>
  </nav>
</header>

<section class="abs hero" role="img" aria-label="Photo of a site engineer in hard hat and hi-vis jacket watching a drone fly over a construction site with a crane">
  <svg class="arrow" style="left:40px" width="24" height="64" viewBox="0 0 24 64"><path d="M22 2L3 32l19 30" stroke="#fff" stroke-width="2.5" fill="none"/></svg>
  <svg class="arrow" style="right:40px" width="24" height="64" viewBox="0 0 24 64"><path d="M2 2l19 30L2 62" stroke="#fff" stroke-width="2.5" fill="none"/></svg>
  <div class="caption">Capture • Process • Deliver</div>
</section>

<section class="abs about">
  <h2 class="heading section-title" style="top:68px">ABOUT PELWICK <small>DRONE SOLUTIONS</small></h2>
  <div class="divider" style="top:127px"></div>
  <p>Lorem ipsum dolor sit amet, consectetur adipiscing elit, sed do eiusmod tempor incididunt ut labore et dolore magna aliqua. Ut enim ad minim veniam, quis nostrud exercitation ullamco laboris nisi ut aliquip ex ea commodo consequat. Duis aute irure dolor in reprehenderit in voluptate velit esse cillum dolore eu fugiat nulla pariatur. Excepteur sint occaecat cupidatat non proident, sunt in culpa qui officia deserunt mollit anim id est laborumLorem ipsum dolor sit amet, consectetur adipiscing elit, sed do eiusmod tempor incididunt ut labore et dolore magna aliqua.</p>
  <a class="btn">READ MORE <i><svg width="10" height="10" viewBox="0 0 10 10"><path d="M3 1l4 4-4 4" stroke="#075d8f" stroke-width="2" fill="none"/></svg></i></a>
</section>

<section class="abs services">
  <h2 class="heading section-title" style="top:70px">OUR <span class="accent">SERVICES</span></h2>
  <div class="divider" style="top:128px"></div>

  <div class="service" style="left:208px">
    <div class="ring"><svg width="52" height="56" viewBox="0 0 52 56"><rect x="6" y="6" width="40" height="48" rx="3" fill="none" stroke="#0b6fa8" stroke-width="3.5"/><rect x="17" y="1" width="18" height="9" rx="2" fill="#0b6fa8"/><g fill="#0b6fa8"><rect x="13" y="19" width="5" height="5"/><rect x="13" y="29" width="5" height="5"/><rect x="13" y="39" width="5" height="5"/><rect x="22" y="20" width="17" height="3"/><rect x="22" y="30" width="17" height="3"/><rect x="22" y="40" width="17" height="3"/></g></svg></div>
    <h3 class="heading">INSPECTIONS</h3>
    <p>Lorem ipsum dolr amet, consectetur adipiscing elit, sed do eiusmod tem incididunt ut labore et.</p>
    <a class="btn">READ MORE <i><svg width="9" height="9" viewBox="0 0 10 10"><path d="M3 1l4 4-4 4" stroke="#075d8f" stroke-width="2" fill="none"/></svg></i></a>
  </div>

  <div class="service" style="left:469px">
    <div class="ring"><svg width="60" height="56" viewBox="0 0 60 56"><rect x="22" y="4" width="34" height="30" fill="none" stroke="#0b6fa8" stroke-width="3.5"/><circle cx="12" cy="10" r="6" fill="#0b6fa8"/><path d="M5 20h14l10 6-2 4-9-4v26h-5V38h-3v14H5z" fill="#0b6fa8"/><path d="M30 25l8-8 5 5 8-9" stroke="#0b6fa8" stroke-width="3" fill="none"/><path d="M36 34l-6 14M44 34l6 14" stroke="#0b6fa8" stroke-width="3"/></svg></div>
    <h3 class="heading">TRAINING</h3>
    <p>Lorem ipsum dolr amet, consectetur adipiscing elit, sed do eiusmod tem incididunt ut labore et.</p>
    <a class="btn">READ MORE <i><svg width="9" height="9" viewBox="0 0 10 10"><path d="M3 1l4 4-4 4" stroke="#075d8f" stroke-width="2" fill="none"/></svg></i></a>
  </div>

  <div class="service" style="left:729px">
    <div class="ring"><svg width="60" height="52" viewBox="0 0 60 52"><path d="M4 22l16-4 20 6 16-5v28l-16 5-20-6-16 4z" fill="#0b6fa8"/><path d="M20 18v28M40 24v28" stroke="#fff" stroke-width="2"/><path d="M30 2a9 9 0 0 0-9 9c0 7 9 17 9 17s9-10 9-17a9 9 0 0 0-9-9z" fill="#0b6fa8" stroke="#fff" stroke-width="2"/><circle cx="30" cy="11" r="3.5" fill="#fff"/></svg></div>
    <h3 class="heading">MAPPING</h3>
    <p>Lorem ipsum dolr amet, consectetur adipiscing elit, sed do eiusmod tem incididunt ut labore et.</p>
    <a class="btn">READ MORE <i><svg width="9" height="9" viewBox="0 0 10 10"><path d="M3 1l4 4-4 4" stroke="#075d8f" stroke-width="2" fill="none"/></svg></i></a>
  </div>

  <div class="service" style="left:990px">
    <div class="ring"><svg width="68" height="44" viewBox="0 0 68 44"><path d="M2 8l12-4 6 18-12 4z" fill="#0b6fa8"/><path d="M66 8l-12-4-6 18 12 4z" fill="#0b6fa8"/><path d="M17 10l11-4 8 3 10-3 6 4-5 14-14 13c-2 2-5 1-6-1l-3-2-3-2-3-3-5-5z" fill="#0b6fa8"/><path d="M30 14l6 3 7-3M26 28l5 4M22 25l5 4M29 31l4 3" stroke="#fff" stroke-width="2" fill="none"/></svg></div>
    <h3 class="heading">CONSULTING</h3>
    <p>Lorem ipsum dolr amet, consectetur adipiscing elit, sed do eiusmod tem incididunt ut labore et.</p>
    <a class="btn">READ MORE <i><svg width="9" height="9" viewBox="0 0 10 10"><path d="M3 1l4 4-4 4" stroke="#075d8f" stroke-width="2" fill="none"/></svg></i></a>
  </div>
</section>

<section class="abs map" role="img" aria-label="Road map of the central United States showing the company location">
  <div class="inset" role="img" aria-label="Photo of a waterfront city skyline at dusk"></div>
</section>

<footer class="abs footer"></footer>

<div class="abs card-left">
  <div class="logo"><span class="dot"></span><span class="name"><b>PELWICK</b><small>DRONE SOLUTIONS</small></span></div>
  <h4>FOLLOW US ON</h4>
  <div class="social" aria-label="Social media links"><span></span><span></span><span></span><span></span><span></span></div>
  <p>Lorem ipsum dolor sit amet, consectetuer adipiscing elit, sed diam nonummy nibh euismod tincidunt ut laoreet dolore magna aliquam erat volutpat. Ut wisi enim ad minim veniam.</p>
</div>

<form class="abs card-right">
  <h2>QUICK INQUIRY</h2>
  <div class="bar"></div>
  <div class="field" style="top:112px">Name</div>
  <div class="field" style="top:163px">Email</div>
  <div class="field" style="top:215px">Subject</div>
  <div class="field" style="top:267px;padding-bottom:34px">Message</div>
  <div class="submit">SUBMIT <i><svg width="10" height="10" viewBox="0 0 10 10"><path d="M3 1l4 4-4 4" stroke="#2a2a2a" stroke-width="2" fill="none"/></svg></i></div>
</form>

<nav class="abs footer-nav">
  <a style="left:327px">HOME</a>
  <a style="left:444px">ABOUT US</a>
  <a style="left:601px">SERVICES</a>
  <a style="left:755px">CONTACT US</a>
</nav>

<div class="info" style="left:285px">
  <div class="badge"><svg width="20" height="26" viewBox="0 0 20 26"><path d="M10 1a9 9 0 0 0-9 9c0 7 9 15 9 15s9-8 9-15a9 9 0 0 0-9-9z" fill="#fff"/><circle cx="10" cy="10" r="3.5" fill="#0b6fa8"/></svg></div>
  123, Lorem ipsum dolor sit amet
</div>
<div class="info" style="left:605px">
  <div class="badge"><svg width="22" height="22" viewBox="0 0 24 24"><path fill="#fff" d="M6.6 10.8a15 15 0 0 0 6.6 6.6l2.2-2.2c.3-.3.7-.4 1-.2 1.1.4 2.3.6 3.6.6.6 0 1 .4 1 1V20c0 .6-.4 1-1 1A17 17 0 0 1 3 4c0-.6.4-1 1-1h3.5c.6 0 1 .4 1 1 0 1.3.2 2.5.6 3.6.1.3 0 .7-.2 1z"/></svg></div>
  615-482-9031
</div>
<div class="info" style="left:923px">
  <div class="badge"><svg width="26" height="22" viewBox="0 0 26 22"><path d="M3 10l10-8 10 8" stroke="#fff" stroke-width="2.5" fill="none"/><rect x="3" y="10" width="20" height="11" fill="none" stroke="#fff" stroke-width="2.5"/><path d="M3 11l10 6 10-6" stroke="#fff" stroke-width="2" fill="none"/></svg></div>
  info@pelwickdronesolutions.example
</div>

<div class="abs rule"></div>
<div class="abs copyright">Copyright © 2018 PELWICK DRONE SOLUTIONS. All Rights Reserved.</div>

</body>
</html>
```